Halvorn spray foam and Environmental

I have business cards but need new ones. The ones I have are very bland. Here is. Y company website http://www.halvornsprayfoam.ca

Also I can send you copies of the current cards
I would also need my current logo on the new design as well.. Also spray foam and Environmental

Industry/Entity Type

Business

Logo Text

Halvorn.

```html
<!DOCTYPE html>
<html lang="en">
<head>
<meta charset="utf-8">
<title>Halvorn business cards</title>
<link rel="stylesheet" href="https://fonts.googleapis.com/css2?family=Open+Sans:wght@400;600;700;800&display=swap">
<style>
  :root {
    --bg: #e4e3e1;
    --card: #fbfbfa;
    --purple: #6a2a8a;
    --purple-soft: #a47bbb;
    --ink: #1c1c1c;
    --slate: #5b5f66;
  }
  * { box-sizing: border-box; margin: 0; padding: 0; }
  html, body { width: 1200px; height: 1000px; overflow: hidden; }
  body {
    background: var(--bg);
    font-family: "Open Sans", Arial, sans-serif;
    color: var(--ink);
    position: relative;
  }
  .card {
    position: absolute;
    width: 560px;
    height: 320px;
    background: var(--card);
    box-shadow: 0 2px 6px rgba(0,0,0,0.12);
    overflow: hidden;
  }
  .card--front { left: 320px; top: 110px; }
  .card--back { left: 320px; top: 530px; }

  .brand { display: flex; align-items: center; gap: 18px; }
  .brand__mark { width: 62px; height: 40px; background: var(--slate); }
  .brand__name {
    font-weight: 800; font-size: 28px; color: var(--purple); letter-spacing: 0.5px;
  }
  .rule { position: absolute; left: 28px; right: 28px; height: 2px; background: var(--purple); }

  /* front */
  .card--front .brand { position: absolute; top: 38px; left: 0; right: 0; justify-content: center; }
  .card--front .rule { top: 108px; }
  .services { position: absolute; top: 124px; left: 0; right: 0; text-align: center; }
  .services__title { font-weight: 800; font-size: 16px; color: var(--purple); margin-bottom: 4px; }
  .services__list { font-size: 12.5px; font-weight: 600; text-transform: uppercase; line-height: 1.35; margin-bottom: 12px; }

  /* back */
  .corner-band {
    position: absolute; top: 0; right: 0; width: 240px; height: 110px;
    background: linear-gradient(100deg, rgba(255,255,255,0) 0%, var(--purple-soft) 60%, var(--purple) 100%);
  }
  .card--back .brand { position: absolute; top: 44px; left: 28px; }
  .card--back .rule { top: 124px; }
  .contact { position: absolute; font-size: 14px; line-height: 1.45; }
  .contact--foam { left: 36px; top: 184px; }
  .contact--enviro { left: 290px; top: 154px; }
  .contact__title { font-weight: 800; font-size: 17px; color: var(--purple); margin-bottom: 8px; }
  .contact__phone { font-weight: 700; }
  .contact b { font-weight: 700; }
</style>
</head>
<body>
  <section class="card card--front">
    <div class="brand">
      <span class="brand__mark"></span>
      <span class="brand__name">HALVORN</span>
    </div>
    <div class="rule"></div>
    <div class="services">
      <h2 class="services__title">SPRAY FOAM</h2>
      <p class="services__list">Roofing foam, slab jacking, 2 pound/ half pound,<br>sound proofing, batt insulation, attic blow in</p>
      <h2 class="services__title">ENVIRONMENTAL</h2>
      <p class="services__list">Air monitoring, asbestos testing, asbestos removal<br>building demolition, lead testing, mould removal</p>
    </div>
  </section>

  <section class="card card--back">
    <div class="corner-band"></div>
    <div class="brand">
      <span class="brand__mark"></span>
      <span class="brand__name">HALVORN</span>
    </div>
    <div class="rule"></div>
    <div class="contact contact--foam">
      <h2 class="contact__title">SPRAY FOAM</h2>
      <p class="contact__phone">(604) 555 - 0148</p>
      <p><b>E</b> : halvornfoam@mailbox.ca</p>
      <p><b>W</b> : www.halvornsprayfoam.ca</p>
    </div>
    <div class="contact contact--enviro">
      <h2 class="contact__title">ENVIRONMENTAL</h2>
      <p class="contact__phone">(604) 555 - 0172</p>
      <p><b>E</b> : halvornenviro1@mailbox.ca</p>
      <p><b>W</b> : www.halvornenvironmental.ca</p>
    </div>
  </section>
</body>
</html>
```